a business advisory consulting website

I need a website 3-5 pages to sell my professional services in IT and Project management Consulting. My company name is Northwell Strategy Consulting. I want it to be device friendly and easy to navigate for the busy executive however intriguing enough.
I have attached some info I drafted on About the company and personal Bio. Also there is a website that I really like that I have attached the initial site pdf and websites that I like are here: https://quillmarshcapital.example, https://tandermoviews.example, https://www.felkinlearningconsulting.example as examples. Thanks
Updates

Hi Designers, I have uploaded the logo in 3D .png format, to assist in the web design.

Target Market(s)

B2B, governments, IT companies, Project Management companies and Consulting firms, small medium enterprises to large corporate enterprises.

Industry/Entity Type

It Professional

Coding

Coded - Design and coding required

Number of Pages Required

5+ page

Font styles to use
Sans Serif

Requirements
Must have
• Home, About company, the team, what we do and contact us
Nice to have
• Blog
Should not have
• pop ups, flash

```html
<!DOCTYPE html>
<html lang="en">
<head>
<meta charset="utf-8">
<title>Northwell Strategy Consulting</title>
<link rel="stylesheet" href="https://fonts.googleapis.com/css2?family=Montserrat:wght@400;500;600;700;800&family=Lato:wght@300;400;700&display=swap">
<style>
:root{
  --red:#e02127;
  --red-dark:#b8181d;
  --navy:#2a3263;
  --navy-deep:#232a55;
  --ink:#222a4d;
  --text:#555;
  --muted:#9a9a9a;
  --light:#f7f7f7;
  --line:#e6e6e6;
  --white:#fff;
}
*{box-sizing:border-box;margin:0;padding:0}
html,body{width:1200px;height:3052px;overflow:hidden}
body{position:relative;font-family:'Lato',sans-serif;color:var(--text);background:var(--white)}
.abs{position:absolute}
h1,h2,h3,h4{font-family:'Montserrat',sans-serif;font-weight:500}
.accent{color:var(--red)}

/* header + hero */
.hero{left:0;top:0;width:1200px;height:675px;background:linear-gradient(180deg,#4a4f57 0%,#5d636a 35%,#3a3d43 70%,#2a2c30 100%)}
.brand{display:flex;align-items:center;gap:8px;font-family:'Montserrat',sans-serif;font-weight:700;color:var(--white);font-size:17px;line-height:1.05;letter-spacing:.5px}
.brand-dot{width:14px;height:14px;background:var(--red)}
.nav{left:436px;top:42px;width:400px;height:14px;font-size:10.5px;letter-spacing:.2px;color:#e4e4e4;font-family:'Lato',sans-serif}
.nav a{color:inherit;text-decoration:none;position:absolute;top:0;white-space:nowrap}
.nav a.active{color:var(--red)}
.phone-btn{left:911px;top:26px;width:128px;height:36px;background:var(--red);border-radius:3px;color:var(--white);font-family:'Montserrat',sans-serif;font-weight:600;font-size:13px;display:flex;align-items:center;justify-content:center;gap:8px}
.hero-kicker{left:0;width:1200px;top:208px;text-align:center;color:#f2f2f2;font-size:19px;font-weight:300}
.hero-tag{font-family:'Montserrat',sans-serif;font-weight:800;color:var(--white);font-size:34px;text-align:center;line-height:44px;letter-spacing:.5px}
.tag-red{left:450px;top:245px;width:300px;height:44px;background:var(--red)}
.tag-light{left:353px;top:296px;width:494px;height:44px;background:rgba(255,255,255,.35)}

/* about */
.about-photo{left:161px;top:734px;width:338px;height:338px;border-radius:50%;background:radial-gradient(circle at 40% 40%,#b98a64,#6c5444 55%,#3b3a44)}
.about-illus{left:569px;top:734px;width:94px;height:89px;background:linear-gradient(135deg,#e0242a 0 50%,#2a3263 50%);border-radius:6px;opacity:.85}
.about-title{left:571px;top:842px;font-size:34px;color:var(--ink)}
.about-copy{left:571px;top:897px;width:462px;font-size:10.8px;line-height:20.2px;color:#8a8a8a}
.btn{background:var(--red);color:var(--white);font-family:'Montserrat',sans-serif;font-weight:600;font-size:14px;display:flex;align-items:center;justify-content:center;border-radius:2px;box-shadow:0 3px 0 var(--red-dark)}
.about-btn{left:570px;top:1034px;width:128px;height:36px}

/* services */
.services{left:0;top:1131px;width:1200px;height:525px;background:linear-gradient(180deg,rgba(58,66,118,.96),rgba(36,44,90,.97)),linear-gradient(90deg,#6a6c80,#3c4268)}
.sec-title{left:0;width:1200px;text-align:center;font-size:35px}
.sec-sub{left:0;width:1200px;text-align:center;font-size:13.5px;line-height:20px}
.service{width:225px;text-align:center;color:var(--white)}
.service svg{display:block;margin:0 auto}
.service h3{font-family:'Montserrat',sans-serif;font-weight:400;font-size:14.5px;line-height:21px;margin-top:18px;height:42px}
.service p{font-size:10.5px;line-height:19px;color:#d8dbe8;margin-top:9px}
.service .more{display:inline-block;margin-top:10px;font-family:'Montserrat',sans-serif;font-size:10.5px;font-weight:600;color:var(--red)}

/* blog */
.card{top:1852px;width:270px;height:343px;background:var(--white);box-shadow:0 1px 8px rgba(0,0,0,.12)}
.card-photo{width:270px;height:180px}
.meta{position:absolute;left:16px;top:200px;display:flex;align-items:center;gap:8px;font-size:11.5px;color:#8a8a8a}
.meta .gap{width:18px}
.card h4{position:absolute;left:16px;top:228px;width:240px;font-family:'Lato',sans-serif;font-weight:400;font-size:15px;line-height:21px;color:#222}
.card p{position:absolute;left:16px;top:283px;width:240px;font-size:10px;line-height:19px;color:#9a9a9a}

/* contact */
.contact{left:0;top:2263px;width:1200px;height:428px;background:var(--light)}
.contact-title{font-size:26px;line-height:30px;color:var(--ink)}
.c-icon{width:38px;height:38px;background:var(--red);border-radius:3px;box-shadow:0 3px 0 var(--red-dark);display:flex;align-items:center;justify-content:center}
.c-label{font-family:'Montserrat',sans-serif;font-size:15.5px;color:var(--ink)}
.c-small{font-size:10.5px;line-height:19px;color:#666}
.c-strong{font-family:'Montserrat',sans-serif;font-weight:600;font-size:14.5px;color:#222}
.field{background:var(--white);border:1px solid #eee;font-size:11px;color:#777;padding:14px 12px}
.form-btn{left:601px;top:2591px;width:194px;height:36px}

/* footer */
.footer{left:0;top:2691px;width:1200px;height:361px;background:var(--navy)}
.f-text{font-size:10.5px;line-height:19px;color:#e5e7f0}
.f-head{font-family:'Montserrat',sans-serif;font-weight:600;font-size:18px;color:var(--red)}
.f-links{list-style:none;font-size:10.5px;line-height:22.5px;color:#e5e7f0}
.f-links li::before{content:"-";margin-right:8px}
.social{width:30px;height:30px;background:var(--red);border-radius:2px;top:2887px}
.subscribe{left:836px;top:2838px;width:203px;height:36px;background:var(--white);border-radius:2px;font-size:10.5px;color:#666;padding:11px 10px}
.sub-btn{right:4px;top:4px;width:28px;height:28px;background:var(--red);border-radius:2px;display:flex;align-items:center;justify-content:center}
.f-rule{left:161px;top:2977px;width:878px;height:1px;background:rgba(255,255,255,.15)}
.copyright{left:0;top:3005px;width:1200px;text-align:center;font-size:9px;color:#a9aec8;letter-spacing:.3px}
</style>
</head>
<body>

<!-- Header and hero -->
<section class="abs hero" role="img" aria-label="Team of consultants meeting around a boardroom table in a glass-walled office"></section>
<div class="abs brand" style="left:161px;top:28px"><span class="brand-dot"></span><span>NORTHWELL<br>STRATEGY</span></div>
<nav class="abs nav">
  <a class="active" style="left:0">HOME</a>
  <a style="left:57px">ABOUT COMPANY</a>
  <a style="left:169px">THE TEAM</a>
  <a style="left:244px">WHAT WE DO</a>
  <a style="left:342px">CONTACT US</a>
</nav>
<svg class="abs" style="left:867px;top:41px" width="16" height="16" viewBox="0 0 16 16"><circle cx="6.5" cy="6.5" r="5" fill="none" stroke="#fff" stroke-width="1.6"/><line x1="10.3" y1="10.3" x2="15" y2="15" stroke="#fff" stroke-width="1.6"/></svg>
<div class="abs phone-btn">
  <svg width="14" height="14" viewBox="0 0 24 24"><path d="M6.6 10.8a15.1 15.1 0 0 0 6.6 6.6l2.2-2.2c.3-.3.7-.4 1-.2 1.1.4 2.3.6 3.6.6.6 0 1 .4 1 1V20c0 .6-.4 1-1 1A17 17 0 0 1 3 4c0-.6.4-1 1-1h3.5c.6 0 1 .4 1 1 0 1.3.2 2.5.6 3.6.1.3 0 .7-.2 1z" fill="#fff"/></svg>
  123.456.7890
</div>
<p class="abs hero-kicker">We are Expert In</p>
<div class="abs tag-red"></div>
<div class="abs tag-light"></div>
<h1 class="abs hero-tag" style="left:0;width:1200px;top:245px">IT AND PROJECT</h1>
<h1 class="abs hero-tag" style="left:0;width:1200px;top:296px">MANAGEMENT CONSULTING</h1>

<!-- About -->
<div class="abs about-photo" role="img" aria-label="Two colleagues reviewing work together at a laptop"></div>
<div class="abs about-illus" role="img" aria-label="Illustration of a presenter sharing an idea with a person at a laptop"></div>
<h2 class="abs about-title">About <span class="accent">Comapny</span></h2>
<p class="abs about-copy">Lorem ipsum dolor sit amet, consectetur adipiscing elit, sed do eiusmod tempor incididunt ut labore et dolore magna aliqua. Ut enim ad minim veniam, quis nostrud exercitation ullamco laboris nisi ut aliquip ex ea commodo consequat. Duis aute irure dolor in reprehenderit ineof voluptate velit esse cillum dolore eu fugiat nulla pariatur. Excepteur sint occaecat cupidatat non proident, sunt in culpa qui officia deserunt mollit anim id est laborum. Nor again is there anyone who loves or pursues or desires to obtain pain of itself, because it is pain</p>
<div class="abs btn about-btn">LEARN MORE</div>

<!-- What we do -->
<section class="abs services" role="img" aria-label="Business team smiling together in a meeting, under a navy tint"></section>
<h2 class="abs sec-title" style="top:1186px;color:var(--white)">What We Do</h2>
<p class="abs sec-sub" style="top:1241px;color:#e3e5ef">Lorem ipsum dolor sit amet, consectetur adipiscing elit, sed do eiusmod<br>tempor incididunt ut &nbsp;laboris aliquip commodo consequat.</p>

<div class="abs service" style="left:151px;top:1318px">
  <svg width="124" height="124" viewBox="0 0 124 124"><path d="M62 4a58 58 0 1 1-41 17" fill="none" stroke="var(--red)" stroke-width="6"/><circle cx="100" cy="20" r="13" fill="#fff"/><path d="M95 25l10-10M99 15h6v6" stroke="var(--red)" stroke-width="2" fill="none"/><g stroke="#fff" stroke-width="2.5" fill="none"><circle cx="45" cy="80" r="5"/><path d="M38 45l8 8M46 45l-8 8M72 80l8 8M80 80l-8 8M50 75q10-30 35-30"/><path d="M79 40l6 5-6 5"/></g></svg>
  <h3>Market<br>Entry</h3>
  <p>Lorem ipsum dolor sit amet, consectetur incididunt ut &nbsp;laboris nisi ut aliquip ex ea commodo consequat.</p>
  <span class="more">LEARN MORE &nbsp;⟶</span>
</div>
<div class="abs service" style="left:376px;top:1318px">
  <svg width="124" height="124" viewBox="0 0 124 124"><path d="M62 4a58 58 0 1 1-41 17" fill="none" stroke="var(--red)" stroke-width="6"/><circle cx="100" cy="20" r="13" fill="#fff"/><path d="M95 25l10-10M99 15h6v6" stroke="var(--red)" stroke-width="2" fill="none"/><g stroke="#fff" stroke-width="2.5" fill="none"><rect x="44" y="38" width="32" height="44" rx="3"/><rect x="54" y="34" width="12" height="7"/><path d="M52 55h16M52 63h16M52 71h10"/><circle cx="76" cy="72" r="7"/></g></svg>
  <h3>Technology Ananlysis within<br>healthcare</h3>
  <p>Lorem ipsum dolor sit amet, consectetur incididunt ut &nbsp;laboris nisi ut aliquip ex ea commodo consequat.</p>
  <span class="more">LEARN MORE &nbsp;⟶</span>
</div>
<div class="abs service" style="left:601px;top:1318px">
  <svg width="124" height="124" viewBox="0 0 124 124"><path d="M62 4a58 58 0 1 1-41 17" fill="none" stroke="var(--red)" stroke-width="6"/><circle cx="100" cy="20" r="13" fill="#fff"/><path d="M95 25l10-10M99 15h6v6" stroke="var(--red)" stroke-width="2" fill="none"/><g stroke="#fff" stroke-width="2.5" fill="none"><path d="M38 60a24 22 0 0 1 48 0zM62 38v46q0 6-6 6t-5-5"/><path d="M50 60l12-22 12 22"/></g></svg>
  <h3>Process Improvement<br>within government</h3>
  <p>Lorem ipsum dolor sit amet, consectetur incididunt ut &nbsp;laboris nisi ut aliquip ex ea commodo consequat.</p>
  <span class="more">LEARN MORE &nbsp;⟶</span>
</div>
<div class="abs service" style="left:826px;top:1318px">
  <svg width="124" height="124" viewBox="0 0 124 124"><path d="M62 4a58 58 0 1 1-41 17" fill="none" stroke="var(--red)" stroke-width="6"/><circle cx="100" cy="20" r="13" fill="#fff"/><path d="M95 25l10-10M99 15h6v6" stroke="var(--red)" stroke-width="2" fill="none"/><g stroke="#fff" stroke-width="2.5" fill="none"><rect x="38" y="42" width="48" height="32" rx="2"/><path d="M54 84h16M62 74v10M62 48q6 6 0 18q-6-12 0-18M57 64l-4 4M67 64l4 4"/></g></svg>
  <h3>Advise for early stage<br>startup</h3>
  <p>Lorem ipsum dolor sit amet, consectetur incididunt ut &nbsp;laboris nisi ut aliquip ex ea commodo consequat.</p>
  <span class="more">LEARN MORE &nbsp;⟶</span>
</div>

<!-- Blog -->
<h2 class="abs sec-title" style="top:1711px;color:var(--ink)">Latest <span class="accent">Blog</span></h2>
<p class="abs sec-sub" style="top:1775px;color:var(--muted)">Lorem ipsum dolor sit amet, consectetur adipiscing elit, sed do eiusmod<br>tempor incididunt ut &nbsp;laboris aliquip commodo consequat.</p>

<article class="abs card" style="left:161px">
  <div class="card-photo" role="img" aria-label="Hands holding a smartphone showing a shopping site" style="background:linear-gradient(135deg,#8c6a4e,#c9b59b 55%,#5d5d62)"></div>
  <div class="meta">
    <svg width="12" height="12" viewBox="0 0 12 12"><rect x="1" y="2" width="10" height="9" fill="none" stroke="var(--red)" stroke-width="1.3"/><path d="M1 5h10M4 1v2M8 1v2" stroke="var(--red)" stroke-width="1.3"/></svg>
    <span>August 12, 2020</span><span class="gap"></span>
    <svg width="12" height="12" viewBox="0 0 12 12"><circle cx="6" cy="3.5" r="3" fill="var(--red)"/><path d="M0 12q6-9 12 0z" fill="var(--red)"/></svg>
    <span>Admin</span>
  </div>
  <h4>Lorem ipsum dolor sit amet, this consectetur adipiscing elit.</h4>
  <p>Lorem ipsum dolor sit amet, consectetur adipiscing elit, sed do eiusmod tempor incididunt.</p>
</article>
<article class="abs card" style="left:464px">
  <div class="card-photo" role="img" aria-label="Two businessmen in suits working at a laptop in an office" style="background:linear-gradient(135deg,#cfd6de,#8e99a6 50%,#3d4450)"></div>
  <div class="meta">
    <svg width="12" height="12" viewBox="0 0 12 12"><rect x="1" y="2" width="10" height="9" fill="none" stroke="var(--red)" stroke-width="1.3"/><path d="M1 5h10M4 1v2M8 1v2" stroke="var(--red)" stroke-width="1.3"/></svg>
    <span>August 12, 2020</span><span class="gap"></span>
    <svg width="12" height="12" viewBox="0 0 12 12"><circle cx="6" cy="3.5" r="3" fill="var(--red)"/><path d="M0 12q6-9 12 0z" fill="var(--red)"/></svg>
    <span>Admin</span>
  </div>
  <h4>Lorem ipsum dolor sit amet, this consectetur adipiscing elit.</h4>
  <p>Lorem ipsum dolor sit amet, consectetur adipiscing elit, sed do eiusmod tempor incididunt.</p>
</article>
<article class="abs card" style="left:769px">
  <div class="card-photo" role="img" aria-label="Open laptop on a wooden desk with a glass beside it" style="background:linear-gradient(135deg,#7a3a1c,#c0682e 45%,#3a2016)"></div>
  <div class="meta">
    <svg width="12" height="12" viewBox="0 0 12 12"><rect x="1" y="2" width="10" height="9" fill="none" stroke="var(--red)" stroke-width="1.3"/><path d="M1 5h10M4 1v2M8 1v2" stroke="var(--red)" stroke-width="1.3"/></svg>
    <span>August 12, 2020</span><span class="gap"></span>
    <svg width="12" height="12" viewBox="0 0 12 12"><circle cx="6" cy="3.5" r="3" fill="var(--red)"/><path d="M0 12q6-9 12 0z" fill="var(--red)"/></svg>
    <span>Admin</span>
  </div>
  <h4>Lorem ipsum dolor sit amet, this consectetur adipiscing elit.</h4>
  <p>Lorem ipsum dolor sit amet, consectetur adipiscing elit, sed do eiusmod tempor incididunt.</p>
</article>

<!-- Contact -->
<section class="abs contact"></section>
<h2 class="abs contact-title" style="left:162px;top:2323px">Our address and <span class="accent">contact</span><br><span class="accent">informations</span></h2>

<div class="abs c-icon" style="left:161px;top:2411px"><svg width="18" height="20" viewBox="0 0 18 20"><path d="M9 1a6 6 0 0 1 6 6c0 5-6 10-6 10S3 12 3 7a6 6 0 0 1 6-6z" fill="none" stroke="#fff" stroke-width="1.8"/><circle cx="9" cy="7" r="2" fill="#fff"/><path d="M4 19h10" stroke="#fff" stroke-width="1.8"/></svg></div>
<p class="abs c-label" style="left:215px;top:2404px">Office Address</p>
<p class="abs c-small" style="left:215px;top:2430px">123,Address, State Name, Street Name, City Name,<br>City Name, Zipcode</p>

<div class="abs c-icon" style="left:161px;top:2500px"><svg width="18" height="18" viewBox="0 0 24 24"><path d="M6.6 10.8a15.1 15.1 0 0 0 6.6 6.6l2.2-2.2c.3-.3.7-.4 1-.2 1.1.4 2.3.6 3.6.6.6 0 1 .4 1 1V20c0 .6-.4 1-1 1A17 17 0 0 1 3 4c0-.6.4-1 1-1h3.5c.6 0 1 .4 1 1 0 1.3.2 2.5.6 3.6.1.3 0 .7-.2 1z" fill="#fff"/></svg></div>
<p class="abs c-label" style="left:215px;top:2498px">Call for help</p>
<p class="abs c-strong" style="left:215px;top:2525px">(123) 456 - 7890</p>

<div class="abs c-icon" style="left:161px;top:2586px"><svg width="18" height="14" viewBox="0 0 18 14"><rect x="1" y="1" width="16" height="12" fill="#fff"/><path d="M1 1l8 7 8-7" stroke="var(--red)" stroke-width="1.5" fill="none"/></svg></div>
<p class="abs c-label" style="left:215px;top:2584px">Call for help</p>
<p class="abs c-strong" style="left:215px;top:2611px;font-size:14px">info@northwellstrategy.example</p>

<h2 class="abs contact-title" style="left:601px;top:2323px">Make an appoinment for<br><span class="accent">free consultation</span></h2>
<div class="abs field" style="left:601px;top:2407px;width:212px;height:43px">First Name :</div>
<div class="abs field" style="left:826px;top:2407px;width:213px;height:43px">Phone :</div>
<div class="abs field" style="left:601px;top:2463px;width:438px;height:43px">Emial :</div>
<div class="abs field" style="left:601px;top:2520px;width:438px;height:57px;padding-top:10px">Message / Comments :</div>
<div class="abs btn form-btn">BOOK AN APPOINTMENT</div>

<!-- Footer -->
<footer class="abs footer"></footer>
<div class="abs brand" style="left:161px;top:2757px"><span class="brand-dot"></span><span>NORTHWELL<br>STRATEGY</span></div>
<p class="abs f-text" style="left:162px;top:2816px;width:195px">Lorem ipsum dolor amet, consectetur adipiscing elit, sed do eiusmod tempor incididunt.</p>
<div class="abs social" style="left:161px" role="img" aria-label="Social link"></div>
<div class="abs social" style="left:199px" role="img" aria-label="Social link"></div>
<div class="abs social" style="left:237px" role="img" aria-label="Social link"></div>

<h4 class="abs f-head" style="left:387px;top:2750px">links</h4>
<ul class="abs f-links" style="left:387px;top:2784px">
  <li>Home</li><li>About company</li><li>The Team</li><li>What We Do</li><li>Contact Us</li>
</ul>
<h4 class="abs f-head" style="left:612px;top:2750px">Help</h4>
<ul class="abs f-links" style="left:612px;top:2784px">
  <li>Blog</li><li>Faqs</li><li>Privacy Policy</li><li>Terms &amp; Conditions</li>
</ul>
<h4 class="abs f-head" style="left:837px;top:2750px">Stay Update</h4>
<p class="abs f-text" style="left:837px;top:2787px;width:200px">Lorem ipsum dolor amet, consectetur adipiscing elit, sed do eiusmod.</p>
<div class="abs subscribe">Enter Email
  <div class="abs sub-btn"><svg width="14" height="14" viewBox="0 0 14 14"><path d="M1 6l12-5-4 12-2-5z" fill="#fff"/></svg></div>
</div>
<div class="abs f-rule"></div>
<p class="abs copyright">Copyright © NORTHWELL STRATEGY PTY LTD - 2020 . All Right Reserved.</p>

</body>
</html>
```